Music CD Design Project - 4 panel

Pop rock / soft rock ballad single CD case artwork.
Female singer in her 20s.
Would like something clean, classic, cool, sexy.

4 panel gatefold card case - Template: http://www.duplimax.com.au/storage/duplimax-artwork-templates/Duplimax%20Gatefold%20Sleeve.pdf

Artwork specifications:
http://www.duplimax.com.au/artwork-cd-dvd-replication/

Target Market(s)

Record Labels & Commercial Radio Stations / Listeners

Industry/Entity Type

Singer

Requirements
Must have
• Must have all 4 panels utilised (Template: http://www.duplimax.com.au/storage/duplimax-artwork-templates/Duplimax%20Gatefold%20Sleeve.pdf )
Must have text included (below) :
_______________________________________________________
COVER TEXT
LIV GORDON
Hollowed

INSIDE TEXT

HOLLOWED
Performed by: Olivia Gordon
Written By: Olivia Gordon, Gregory L. Hoyle, Owen Marsh
Recorded in Sydney NSW, produced, engineered and mixed by Gregory L. Hoyle. Drums: Lucien Morvantal. Vocals recorded at Drift Studio, Perth WA.

BORROWED SMILES
Written By: Olivia Gordon, Gregory L. Hoyle
Produced and Mixed: Gregory Hoyle at Gregory Hoyle Studio, Sydney, New South Wales. Drums: Lucien Morvantal.

BACK TEXT
Track 1: Hollowed
Track 2: Hollowed [Radio Edit]
Track 3: Borrowed Smiles

www.LivGordonMusic.com
Photography: Bronwyn Kay Photography / Tess Voranne Photography
_____________________________________________________
I have attached photos please use whatever you think will suit.
Inside text can be small print, I just need it there but doesn't have to be the feature / main item.
Nice to have
• LYRICS

HOLLOWED
You're in my picture frame / In black and white before the night you went away / I can't forget that day / My heart I heart it break / Like glass it fell and shattered silently / Your words cut violently / Left me to bleed / Stripped bare of my innocence / Your scent lingers on me / Sounds of an ambulance as my heart it screams / I wished for a nightmare / I prayed for the sun / Not even its warmth could heal me / And it's HOLLOWED to wish upon a star / HOLLOWED to wonder where you are / HOLLOWED I gotta change my tune / It's HOLLOWED I'm not wasting my time on you / Here comes another moon / Tell me how many nights did I cry for you / These tears of truth / Sunrise to sunsets I still remain / A prisoner to my bed for days, afraid / Because life is a maze without you / I taste the tears along my lips / Stuck in this solar eclipse / The day will end without my best friend / I wished for a nightmare / I prayed for the sun / Not even its warmth could heal me / And it's HOLLOWED to wish upon a star / HOLLOWED to wonder where you are / HOLLOWED I gotta change my tune / It's HOLLOWED I'm not wasting my time on you / Here comes another moon / Tell me how many nights did I cry for you / These tears of truth / Sunrise to sunsets I still remain / A prisoner to my bed for days, afraid / Because life is a maze without you / And it's HOLLOWED to wish upon a star / HOLLOWED to wonder where you are / HOLLOWED I gotta change my tune / It's HOLLOWED I'm not wasting my time on you.

BORROWED SMILES
Hello Pinnochio, your other woman called / So cut your nose to spite your face / Your double mask will be defaced / Lying through your wooden teeth / Your puppet pants on fire / There's no real man underneath / You're one IMPRESSIVE LIAR / You think I'm blind, but I have eyes / I see right through your BORROWED SMILES / The faith I had has now expired / Thrown out with your porky pies / This time I can't ignore I won't take it anymore / I'm calling your bluff cos I've had enough of your BORROWED SMILES/ You're running late again, repeating that same old story / Improvisation of fiction, your compulsive addiction / Does nothing for me / Lost in a labyrinth of lies / Your tangled web on fire / Remembering every alibi / You're one IMPRESSIVE LIAR / You think I'm blind, but I have eyes / I see right through your BORROWED SMILES / The faith I had has now expired / Thrown out with your porky pies / This time I can't ignore I won't take it anymore / I'm calling your bluff cos I've had enough of your BORROWED SMILES / Words thrown around a thousand times / Promises are made and tossed aside / You think I'm wrapped around your finger / But I'm leaving you behind / You think I'm blind, but I have eyes / I see right through your BORROWED SMILES / The faith I had has now expired / Thrown out with your porky pies / This time I can't ignore I won't take it anymore / I'm calling your bluff cos I've had enough of your IMPRESSIVE / I'm calling your bluff cos I've had enough of your BORROWED SMILES

```html
<!DOCTYPE html>
<html lang="en">
<head>
<meta charset="utf-8">
<title>Hollowed – Inside Credits Panel</title>
<link href="https://fonts.googleapis.com/css2?family=Open+Sans:ital,wght@0,300;1,300&display=swap" rel="stylesheet">
<style>
  :root {
    --grass-light: #a4bf5a;
    --grass-mid: #5f8f3c;
    --grass-deep: #2f5a2c;
    --grass-shadow: #244a28;
    --grass-low: #6e9b45;
    --credit-text: #f4f7ef;
    --cutout: #ffffff;
    --dash: #3c5a3c;
    --fold-line: rgba(255, 255, 255, 0.28);
  }
  * { margin: 0; padding: 0; box-sizing: border-box; }
  html, body { width: 1200px; height: 1000px; overflow: hidden; }
  body { font-family: "Open Sans", sans-serif; }

  .panel {
    position: relative;
    width: 1200px;
    height: 1000px;
    overflow: hidden;
  }

  .panel__photo {
    position: absolute;
    inset: 0;
    background:
      linear-gradient(180deg,
        var(--grass-light) 0%,
        #8fb04f 8%,
        var(--grass-mid) 14%,
        var(--grass-deep) 20%,
        #4d7c38 26%,
        var(--grass-shadow) 31%,
        #416d33 38%,
        var(--grass-mid) 45%,
        var(--grass-deep) 52%,
        #557f3b 60%,
        var(--grass-low) 68%,
        #4f7d3a 76%,
        var(--grass-low) 84%,
        #5a8a3e 92%,
        #679745 100%);
  }

  .panel__fold {
    position: absolute;
    top: 0;
    left: 1163px;
    width: 1px;
    height: 1000px;
    background: var(--fold-line);
  }

  .panel__slot {
    position: absolute;
    top: 0;
    left: 0;
    width: 80px;
    height: 1000px;
  }

  .credits {
    position: absolute;
    top: 342px;
    left: 148px;
    width: 960px;
    color: var(--credit-text);
    font-weight: 300;
    font-size: 21.5px;
    line-height: 32.5px;
    letter-spacing: -0.4px;
    text-transform: uppercase;
  }
  .credits__track { margin-bottom: 32px; }
  .credits__title { font-style: italic; }
</style>
</head>
<body>
  <main class="panel">
    <div class="panel__photo" role="img" aria-label="Softly blurred photograph of a green grassy field"></div>
    <div class="panel__fold"></div>

    <svg class="panel__slot" viewBox="0 0 80 1000" aria-hidden="true">
      <path d="M0 0 L6 0 Q122 500 0 1000 Z" fill="var(--cutout)"/>
      <path d="M0 95 Q84 480 0 880" fill="none" stroke="var(--dash)" stroke-width="2" stroke-dasharray="10 13"/>
    </svg>

    <section class="credits">
      <div class="credits__track">
        <p class="credits__title">Hollowed</p>
        <p>Performed by: Olivia Gordon</p>
        <p>Written by: Olivia Gordon, Gregory L. Hoyle, Owen Marsh</p>
        <p>Recorded in Sydney NSW, produced, engineered and mixed by Gregory L. Hoyle.</p>
        <p>Drums: Lucien Morvantal. Vocals recorded at Drift Studio, Perth WA.</p>
      </div>
      <div class="credits__track">
        <p class="credits__title">Borrowed Smiles</p>
        <p>Performed by: Olivia Gordon</p>
        <p>Written by: Olivia Gordon, Gregory L. Hoyle</p>
        <p>Produced and mixed: Gregory Hoyle at Gregory Hoyle Studio, Sydney, New South Wales. Drums: Lucien Morvantal.</p>
      </div>
    </section>
  </main>
</body>
</html>
```